Website Design for Korvinel.com.au (Design + Code)

I am a small business specialising in aquarium monitoring solutions.
Our products essentially are computerised monitoring equipment for aquariums. E.g. https://www.reeflowgauge.com/en-GB/products-shop/marivex-controllers
and also TalMow http://www.talmow.com/
I see the design having 3 pages
* Landing / Home
* Gallery
* Contact us
Design:
I am looking for a cutting edge slick looking site. It should have a number of pages so the site is interactive with contact us, gallery etc.
I have attached our logo and can provide more info as requested. I will be constantly changing the site content as well from my end.
I have attached my logo design which was done via PixelGuild. It can be changed/altered if you feel something else would work better
Final deliverable:
* This project requires both design and development (coding).
* The 3 design pages are to be delivered as PSD files, and the coding as HTML.
The site will need to scale to be viewable on both iPhone/ipads etc as well as standard desktop
Updates
Hi All,
Just based on the couple of designs that have come through so far I would like to specify that for the front landing page, I don't want to be product specific, but rather a page that describes the company and some information about what we do and why it is important to monitor your aquarium. It would still be good to have some images of the monitoring equipment, I will provide or modify the text with the information I am talking about above.
I hope this a little more specific.
Hi All,
While I like the designs that are coming through, I still feel that they are all very template based in look and feel.
I am looking for a unique design that is interactive and engaging to the viewer.
If you need more information from me, please let me know.
Please feel free to submit completely new designs.
Kind Regards,
Rupert
Industry/Entity Type
Small Business

```html
<!DOCTYPE html>
<html lang="en">
<head>
<meta charset="utf-8">
<title>Korvinel – Aquarium Monitoring Solutions</title>
<link rel="stylesheet" href="https://fonts.googleapis.com/css2?family=Inter:wght@400;500;600;700&display=swap">
<style>
:root{
  --page-bg:#f6f6f6;
  --panel:#ffffff;
  --blue:#4aa8df;
  --blue-dark:#2d8fcc;
  --ink:#1f1f1f;
  --text:#333333;
  --muted:#8a8a8a;
  --grey-dark:#545454;
  --grey-mid:#6e6e6e;
  --line:#d9d9d9;
  --product-bg:#eaf4fa;
  --field:#ffffff;
  --field-soft:#eef6fc;
}
*{box-sizing:border-box;margin:0;padding:0}
html,body{width:1102px;height:1200px;overflow:hidden}
body{background:var(--page-bg);font-family:"Inter",Helvetica,Arial,sans-serif;color:var(--text);position:relative}
.abs{position:absolute}

/* header */
.brand{left:140px;top:24px;display:flex;align-items:center;gap:12px}
.brand-mark{width:34px;height:34px;background:var(--blue)}
.brand-name{font-size:34px;font-weight:500;color:var(--grey-mid);letter-spacing:-0.5px;line-height:1}
.brand-tag{left:192px;top:80px;font-size:8px;color:var(--blue);letter-spacing:0.4px}
.social-top{left:851px;top:17px;display:flex;gap:8px}
.social-dot{width:26px;height:26px;border-radius:50%;border:1.5px solid #c9c9c9}
.phone-top{left:802px;top:64px;display:flex;align-items:center;gap:6px;font-size:17px;font-weight:500;color:var(--grey-dark)}

/* navigation */
.nav{left:142px;top:105px;width:805px;height:37px;background:var(--blue)}
.nav a{position:absolute;top:0;height:37px;line-height:37px;color:#fff;font-size:13.5px;font-weight:600;text-decoration:none}
.nav a.active{background:var(--grey-dark);width:76px;left:0;text-align:center}

/* hero */
.hero{left:142px;top:142px;width:805px;height:309px;background:linear-gradient(180deg,#1a6fb8 0%,#0d5aa6 45%,#06417f 100%)}
.hero-title{left:162px;top:186px;font-size:43px;font-weight:600;color:#fff;letter-spacing:-0.5px}
.hero-text{left:162px;top:231px;width:450px;font-size:13.2px;font-weight:600;line-height:21px;color:#fff}
.hero-dots{left:800px;top:413px;display:flex;align-items:center;gap:6px}
.hero-dots .dot{width:10px;height:10px;border-radius:50%;background:#fff}

/* main panel */
.main{left:142px;top:451px;width:805px;height:579px;background:var(--panel)}
.footer{left:142px;top:1030px;width:805px;height:102px;background:linear-gradient(180deg,#f4f4f4,#eaeaea);border-top:1px solid #e2e2e2;box-shadow:0 3px 4px rgba(0,0,0,.18)}

.welcome{left:162px;top:473px;width:511px;height:258px;border:1px solid var(--line);background:#fff;padding:18px 13px}
.welcome h1{font-size:17px;font-weight:600;color:var(--ink);margin-bottom:12px;letter-spacing:-0.2px}
.welcome p{font-size:10.6px;line-height:17px;color:var(--text)}
.welcome p + p{margin-top:17px}
.read-more{display:block;margin-top:17px;font-size:10.6px;color:var(--blue);text-decoration:none}

.quick{left:694px;top:473px;width:231px;height:258px;background:var(--grey-dark)}
.box-head{height:41px;background:var(--blue);color:#fff;font-size:17px;font-weight:500;padding:0 13px;line-height:41px;position:relative}
.box-head svg{position:absolute;right:12px;top:10px}
.field{position:absolute;left:14px;width:203px;background:var(--field);font-size:10.5px;color:var(--ink);padding:6px 7px}
.field.msg{background:var(--field-soft)}
.btn{display:block;background:var(--blue);color:#fff;font-size:11px;font-weight:500;text-align:center;border:1px solid var(--blue-dark)}
.send{position:absolute;left:68px;top:218px;width:91px;height:25px;line-height:23px}

.news{left:162px;top:754px;width:232px;height:234px;border:1px solid var(--line);background:#fff}
.news-item{position:absolute;left:13px;display:flex;gap:7px}
.thumb{width:41px;height:41px;background:linear-gradient(135deg,#8a6a48,#c9a07a);flex:none}
.news-text{font-size:10.4px;line-height:14px;color:var(--text);width:160px}
.news-text span{color:var(--blue)}

.products{left:414px;top:754px;width:511px;height:234px;border:1px solid #d6e6f1;background:var(--product-bg)}
.product{position:absolute;top:62px;width:120px;text-align:center}
.product-shot{height:64px;margin:0 auto 8px;background:linear-gradient(180deg,#3c3c3c,#111);border-radius:4px}
.product-name{font-size:10.5px;color:var(--text)}
.price{font-size:10.5px;color:var(--blue);margin-top:4px}
.buy{width:92px;height:25px;line-height:23px;margin:6px auto 0}

.foot-brand{left:162px;top:1066px;font-size:17px;font-weight:500;color:var(--grey-mid)}
.foot-info{left:142px;top:1048px;width:805px;text-align:center;font-size:10.5px;color:var(--muted);line-height:16px}
.foot-info b{color:var(--ink);font-weight:600}
.foot-social{left:499px;top:1088px;display:flex;gap:8px}
.foot-social .social-dot{border:1.8px solid #555}
.foot-social .social-dot.on{border-color:var(--blue)}
</style>
</head>
<body>

<header>
  <div class="abs brand"><span class="brand-mark"></span><span class="brand-name">Korvinel</span></div>
  <div class="abs brand-tag">AQUARIUM MONITORING SOLUTIONS</div>
  <div class="abs social-top" aria-label="Social links"><span class="social-dot"></span><span class="social-dot"></span><span class="social-dot"></span></div>
  <div class="abs phone-top">
    <svg width="26" height="26" viewBox="0 0 26 26" aria-hidden="true"><circle cx="13" cy="13" r="11.5" fill="none" stroke="#4aa8df" stroke-width="2"/><path d="M9 7.5c.8-.5 1.6-.3 2 .4l1.1 2c.3.6.1 1.2-.4 1.6l-.8.6c.6 1.5 1.7 2.7 3.1 3.4l.7-.8c.4-.5 1.1-.6 1.6-.3l2 1.2c.6.4.8 1.2.3 1.9l-.7.9c-.6.7-1.6 1-2.5.6-3.3-1.3-5.9-3.9-7.2-7.2-.4-.9-.1-1.9.6-2.5z" fill="#4aa8df"/></svg>
    0291 - 47 82 16
  </div>
</header>

<nav class="abs nav">
  <a class="active" href="#">Home</a>
  <a href="#" style="left:92px">About us</a>
  <a href="#" style="left:182px">Products &amp; Service</a>
  <a href="#" style="left:332px">Gallery</a>
  <a href="#" style="left:393px">Solutions</a>
  <a href="#" style="left:486px">Contact</a>
</nav>

<section class="abs hero" role="img" aria-label="Underwater photograph of a sea turtle and fish swimming in deep blue water"></section>
<h2 class="abs hero-title">The Astounding Lives.</h2>
<p class="abs hero-text">You can play a critical role in inspiring conservation of the oceans by joining one of our esteemed Donor Circles, including us in your estate plan or becoming a Business Partner.</p>
<div class="abs hero-dots">
  <span class="dot"></span><span class="dot"></span><span class="dot"></span><span class="dot"></span><span class="dot"></span>
  <svg width="20" height="20" viewBox="0 0 20 20" aria-hidden="true"><circle cx="10" cy="10" r="8.5" fill="none" stroke="#fff" stroke-width="1.8"/><path d="M11.5 6l-4 4 4 4z" fill="#fff"/></svg>
  <svg width="20" height="20" viewBox="0 0 20 20" aria-hidden="true"><circle cx="10" cy="10" r="8.5" fill="none" stroke="#4aa8df" stroke-width="1.8"/><path d="M8.5 6l4 4-4 4z" fill="#4aa8df"/></svg>
</div>

<main class="abs main"></main>

<article class="abs welcome">
  <h1>Welcome to Korvinel Aquarium Monitoring</h1>
  <p>Mijn naam is Mirthe Valkenburg en ik ben 25 jaar oud. Vanaf februari 2012 ben ik begonnen aan de opleiding voor pedicure, deze opleiding volg ik bij<br>Varenhof-opleidingen in Rotterdam.</p>
  <p>het is nu mei en ik ben geslaagd voor mijn laatste theorie examen!! vanaf 20 mei kan ik opgeroepen worden voor het praktijk examen dus dat schiet ook al op.<br>ik heb het afgelopen jaar erg veel geleerd en er valt nog veel meer te leren in dit vak, wat ik ook zeker wil blijven doen.</p>
  <a class="read-more" href="#">Read more</a>
</article>

<aside class="abs quick">
  <div class="box-head">Quick Contact
    <svg width="26" height="20" viewBox="0 0 26 20" aria-hidden="true"><rect x="1" y="4" width="24" height="15" fill="#1e6fa6"/><path d="M1 4l12 9 12-9" fill="none" stroke="#fff" stroke-width="1.5"/><path d="M8 4l5-3 5 3" fill="none" stroke="#1e6fa6" stroke-width="1.5"/></svg>
  </div>
  <div class="field" style="top:54px;height:27px">Name</div>
  <div class="field" style="top:93px;height:27px">Phone no.</div>
  <div class="field" style="top:133px;height:27px">Email</div>
  <div class="field msg" style="top:173px;height:38px">Your enquire.</div>
  <span class="btn send">Send</span>
</aside>

<section class="abs news">
  <div class="box-head">Latest news
    <svg width="22" height="22" viewBox="0 0 22 22" aria-hidden="true"><rect x="2" y="2" width="16" height="18" fill="none" stroke="#1e6fa6" stroke-width="2"/><path d="M5 6h5M5 10h10M5 13h10M5 16h10" stroke="#1e6fa6" stroke-width="1.6"/><path d="M18 6h2v14h-2" fill="none" stroke="#1e6fa6" stroke-width="2"/></svg>
  </div>
  <div class="news-item" style="top:51px"><span class="thumb" role="img" aria-label="Portrait thumbnail"></span><p class="news-text">Mijn naam is Mirthe Valkenburg en ik ben 25 jaar oud. Vanaf februari<br><span>Posted on 17-08-2014</span></p></div>
  <div class="news-item" style="top:105px"><span class="thumb" role="img" aria-label="Portrait thumbnail"></span><p class="news-text">Mijn naam is Mirthe Valkenburg en ik ben 25 jaar oud. Vanaf februari<br><span>Posted on 17-08-2014</span></p></div>
  <div class="news-item" style="top:160px"><span class="thumb" role="img" aria-label="Portrait thumbnail"></span><p class="news-text">Mijn naam is Mirthe Valkenburg en ik ben 25 jaar oud. Vanaf februari<br><span>Posted on 17-08-2014</span></p></div>
</section>

<section class="abs products">
  <div class="box-head">Our products</div>
  <svg class="abs" style="left:13px;top:124px" width="20" height="20" viewBox="0 0 20 20" aria-hidden="true"><circle cx="10" cy="10" r="8.5" fill="#fff" stroke="#9a9a9a" stroke-width="1.4"/><path d="M11.5 6.5l-4 3.5 4 3.5z" fill="#9a9a9a"/></svg>
  <svg class="abs" style="left:477px;top:124px" width="20" height="20" viewBox="0 0 20 20" aria-hidden="true"><circle cx="10" cy="10" r="8.5" fill="#fff" stroke="#9a9a9a" stroke-width="1.4"/><path d="M8.5 6.5l4 3.5-4 3.5z" fill="#9a9a9a"/></svg>
  <div class="product" style="left:34px"><div class="product-shot" style="width:104px" role="img" aria-label="Black expansion box monitoring unit"></div><div class="product-name">Marivex Controller</div><div class="price">€34,59</div><span class="btn buy">Buy</span></div>
  <div class="product" style="left:193px"><div class="product-shot" style="width:92px;background:linear-gradient(180deg,#4a4a4a,#222)" role="img" aria-label="Controller with blue display screen"></div><div class="product-name">Marivex Controller</div><div class="price">€34,59</div><span class="btn buy">Buy</span></div>
  <div class="product" style="left:354px"><div class="product-shot" style="width:92px" role="img" aria-label="Black aquarium controller unit"></div><div class="product-name">Marivex Controller</div><div class="price">€34,59</div><span class="btn buy">Buy</span></div>
</section>

<footer>
  <div class="abs footer"></div>
  <div class="abs foot-brand">Korvinel</div>
  <div class="abs foot-info">
    <b>Phone.</b> : 0291 - 47 82 16 &nbsp; | &nbsp; <b>Mob.</b>: 06 - 58 12 90 47 &nbsp; | &nbsp; <b>E-mail</b>: info@korvinel.com.au<br>
    © All Rights Reserved <b>Korvinel</b>
  </div>
  <div class="abs foot-social" aria-label="Social links"><span class="social-dot"></span><span class="social-dot on"></span><span class="social-dot"></span></div>
</footer>

</body>
</html>
```